Web Design Project for an operational risk management consulting company

Website is for a consulting company specialising in operational risk management. Our specialist areas include crisis and emergency management, community engagement, safety and security. We work internationally, generally in high hazard environments. We are a highly ethical and professional company which prides itself on delivering a strong level of customer service.

As a company we recognise that the key to keeping people safe is ensuring that they work in an ethical and sustainable manner. Therefore we are as much about soft skills as we are about hard skills. We would like our website and supporting images to reflect this.
We have worked throughout Africa and the Middle east, as well as Asia pacific. An international flavour to the website would also be great.
Background images on www.corvellpartnersglobal.com are a good example of what we are thinking of, though very open to fresh ideas.

Target Market(s)

Our customers are generally medium to large organisations who work internationally. We would like to also support more not for profits and non government organisations who work in hazardous environments

Industry/Entity Type

It Company

Number of Pages Required

5+ page

Font styles to use
Sans Serif

Requirements
Must have
• Easy to edit by non IT people
• Section for blogs/news updates
• Pages should include:
• (A) home page
• (B) about us
• (C) services
• (D) contact
• (E) insights
Nice to have
• An international and professional theme. Some gritty images that symbolise the risks associated with working in unstable environments, as well as some human ones and that of the environment
Should not have
• Cartoonish or generic images
• Not focus on traditional physical security aspects

```html
<!DOCTYPE html>
<html lang="en">
<head>
<meta charset="utf-8">
<title>Kestrel Risk – Home</title>
<link rel="stylesheet" href="https://fonts.googleapis.com/css2?family=Open+Sans:wght@400;600;700&display=swap">
<style>
:root{
  --blue:#1d6fbd;
  --blue-dark:#155a9c;
  --navy:#2c3a4a;
  --ink:#333b44;
  --muted:#6e757c;
  --grey-bg:#eef0f2;
  --card-bg:#e4e7ea;
  --footer:#1f2225;
  --white:#ffffff;
}
*{box-sizing:border-box;margin:0;padding:0}
html,body{width:1200px;height:2660px;overflow:hidden}
body{font-family:"Open Sans",Arial,sans-serif;color:var(--ink);background:var(--white);position:relative}
.site-header{position:absolute;left:0;top:0;width:1200px;height:92px;background:var(--white);border-bottom:1px solid #e2e5e8}
.brand{position:absolute;left:70px;top:18px;display:flex;align-items:center;gap:10px}
.brand-mark{width:34px;height:34px;border-radius:50%;background:var(--blue)}
.brand-name{font-size:24px;font-weight:700;color:var(--navy)}
.main-nav{position:absolute;right:70px;top:56px;display:flex;gap:0}
.main-nav a{display:block;padding:8px 24px;font-size:12px;font-weight:600;color:var(--navy);text-decoration:none;letter-spacing:.5px;border-bottom:3px solid transparent}
.main-nav a.active{color:var(--blue);border-bottom-color:var(--blue)}
.social-top{position:absolute;right:78px;top:14px;display:flex;gap:10px}
.social-top span{width:24px;height:24px;background:var(--navy);transform:rotate(45deg);display:block}
.hero{position:absolute;left:0;top:92px;width:1200px;height:540px;background:linear-gradient(180deg,#2f4c78 0%,#5f7fa8 38%,#8e9fb6 55%,#3f5068 75%,#1b2433 100%)}
.hero-content{position:absolute;left:0;top:180px;width:1200px;text-align:center;color:var(--white)}
.hero h1{font-size:46px;font-weight:700;letter-spacing:2px}
.hero p{font-size:24px;margin-top:12px}
.btn-outline{display:inline-block;margin-top:36px;border:2px solid var(--white);color:var(--white);padding:14px 26px;font-size:15px;font-weight:600;letter-spacing:1px}
.features{position:absolute;left:0;top:632px;width:1200px;height:520px;background:var(--grey-bg)}
.feature{position:absolute;top:120px;width:280px;height:290px;background:var(--white);text-align:center;padding:92px 24px 0;box-shadow:0 2px 6px rgba(0,0,0,.08)}
.feature .thumb{position:absolute;left:95px;top:-40px;width:90px;height:90px;border-radius:50%;border:4px solid var(--white);background:linear-gradient(135deg,#c9d6e2,#7d97b3)}
.feature h3{font-size:26px;font-weight:600;color:var(--blue)}
.feature p{font-size:12px;line-height:18px;color:var(--muted);margin-top:10px}
.btn-small{display:inline-block;margin-top:20px;background:var(--blue);color:var(--white);font-size:10px;font-weight:700;padding:6px 14px;letter-spacing:.5px}
.feature.highlight{top:80px;height:350px;background:var(--blue);padding-top:110px}
.feature.highlight h3,.feature.highlight p{color:var(--white)}
.feature.highlight .thumb{top:-20px;border-radius:0;width:150px;left:65px;background:linear-gradient(135deg,#e1e8ef,#8aa2bc)}
.feature.highlight .btn-small{background:var(--white);color:var(--blue)}
.feature.plain h3{color:var(--muted)}
.about{position:absolute;left:0;top:1152px;width:1200px;height:620px;background:#f4f5f6}
.about-block{position:absolute;width:520px}
.about-block h2{font-size:28px;font-weight:400;color:var(--navy);display:flex;align-items:center;gap:12px}
.about-block h2 .icon{width:32px;height:32px;border-radius:50%;background:var(--blue);flex:none}
.about-block p{font-size:13px;line-height:21px;color:var(--muted);margin-top:14px}
.about-block .btn-small{float:right;background:var(--navy)}
.photo{position:absolute;box-shadow:0 2px 8px rgba(0,0,0,.15)}
.blog-news{position:absolute;left:0;top:1772px;width:1200px;height:528px;background:var(--white)}
.col-title{position:absolute;top:70px;font-size:28px;font-weight:700;color:var(--navy);letter-spacing:1px}
.col-title:after{content:"";display:block;width:430px;height:2px;background:#d8dde2;margin-top:10px}
.post{position:absolute;top:160px;width:510px;height:330px;background:var(--card-bg);padding:28px 60px 0 32px}
.post h4{font-size:15px;font-weight:700;color:var(--blue);letter-spacing:.5px}
.post .meta{font-size:12px;color:var(--navy);font-weight:600;margin-top:4px}
.post p{font-size:12px;line-height:19px;color:var(--muted);margin-top:14px}
.post .arrow{position:absolute;right:-18px;top:130px;width:36px;height:60px;background:var(--navy)}
.date-badge{position:absolute;left:28px;top:28px;width:66px;height:66px;background:var(--blue);color:var(--white);font-size:11px;text-align:center;padding-top:16px;line-height:16px;font-weight:600}
.site-footer{position:absolute;left:0;top:2300px;width:1200px;height:360px;background:var(--footer);color:#cfd3d7;text-align:center}
.site-footer h2{font-size:26px;font-weight:600;color:var(--white);margin-top:50px}
.social-row{display:flex;justify-content:center;gap:16px;margin-top:26px}
.social-row span{width:36px;height:36px;border-radius:50%;border:1px solid #7b8188;display:block}
.subscribe-note{font-size:12px;margin-top:24px}
.subscribe-input{width:560px;height:40px;margin:14px auto 0;background:#3a3f44;text-align:left;padding:11px 14px;font-size:12px;color:#9aa0a6}
.btn-subscribe{display:inline-block;margin-top:24px;border:1px solid var(--white);color:var(--white);padding:10px 30px;font-size:13px;font-weight:600}
.copyright{position:absolute;bottom:18px;left:0;width:1200px;font-size:11px;color:#8c9298}
</style>
</head>
<body>
<header class="site-header">
  <div class="brand"><span class="brand-mark"></span><span class="brand-name">Kestrel Risk</span></div>
  <div class="social-top"><span></span><span></span><span></span><span></span></div>
  <nav class="main-nav">
    <a class="active" href="#">HOME PAGE</a><a href="#">ABOUT US</a><a href="#">SERVICES</a><a href="#">CONTACT</a><a href="#">INSIGHTS</a>
  </nav>
</header>

<section class="hero" role="img" aria-label="Mountain lake landscape at dusk">
  <div class="hero-content">
    <h1>HOW PEOPLE KNOW YOU?</h1>
    <p>We, online Marketing &amp; Social Media Consultation is on the house</p>
    <span class="btn-outline">CLAIM FREE CONSULTATION</span>
  </div>
</section>

<section class="features">
  <div class="feature" style="left:150px">
    <div class="thumb" role="img" aria-label="Team member portrait"></div>
    <h3>WHO WE ARE</h3>
    <p>Ihr Ansprechpartner für alle Anliegen rund um Risiko und Sicherheit<br>Hauptstraße 12<br>Büro Nord, Etage 3<br>10115 Musterstadt</p>
    <span class="btn-small">LEARN MORE</span>
  </div>
  <div class="feature highlight" style="left:460px">
    <div class="thumb" role="img" aria-label="Consultants at work"></div>
    <h3>WHAT WE DO</h3>
    <p>Lösungen für das gesamte Spektrum der Risikoberatung in allen Bereichen der Sicherheit.</p>
    <p>Lösungen für das gesamte Spektrum der Krisenvorsorge und des Notfallmanagements weltweit.</p>
    <span class="btn-small">LEARN MORE</span>
  </div>
  <div class="feature plain" style="left:770px">
    <div class="thumb" role="img" aria-label="Client meeting"></div>
    <h3>WHY CHOOSE</h3>
    <p>Wir bieten Ihnen erfahrene Beratung mit klaren Prozessen, verlässlichen Partnern und nachhaltigen Ergebnissen für jedes Projekt vor Ort.</p>
    <span class="btn-small">LEARN MORE</span>
  </div>
</section>

<section class="about">
  <div class="about-block" style="left:100px;top:60px">
    <h2><span class="icon"></span>Lorem Ipsum is simply dummy text</h2>
    <p>Die Beratungsgesellschaft steht für erfahrene Spezialisten im Bereich Risiko und Sicherheit. Wir beraten und unterstützen Sie bei der Planung, Umsetzung und Bewertung Ihrer Projekte in schwierigen Umgebungen. Unser Team verbindet fachliche Kompetenz mit Verständnis für Menschen und Gemeinschaften vor Ort, damit Ihre Mitarbeiter sicher und nachhaltig arbeiten können.</p>
    <span class="btn-small">READ MORE</span>
  </div>
  <div class="photo" style="left:680px;top:30px;width:430px;height:250px;background:linear-gradient(135deg,#c7d3df,#6f8296 60%,#3c4856)" role="img" aria-label="Business team standing in an office"></div>
  <div class="photo" style="left:90px;top:290px;width:440px;height:300px;background:linear-gradient(135deg,#e8dccb,#b89c7c 55%,#6f5a48)" role="img" aria-label="Students learning at desks"></div>
  <div class="about-block" style="left:600px;top:320px">
    <h2><span class="icon"></span>Lorem Ipsum is simply dummy text</h2>
    <p>Sicherheit beruht auf Erfahrung und Vertrauen. Wir begleiten Organisationen von der ersten Analyse bis zur laufenden Betreuung und entwickeln Lösungen, die zu Ihren Zielen passen. Dabei setzen wir auf offene Kommunikation, klare Verantwortlichkeiten und eine enge Zusammenarbeit mit lokalen Partnern.</p>
    <span class="btn-small">READ MORE</span>
  </div>
</section>

<section class="blog-news">
  <h2 class="col-title" style="left:70px">LATEST BLOG</h2>
  <h2 class="col-title" style="left:620px">LATEST NEWS</h2>
  <article class="post" style="left:70px">
    <h4>THERE ARE VARIATIONS OF PASSAGES</h4>
    <div class="meta">By author, 24 June</div>
    <p>Field teams working in remote regions face changing conditions every day. In this post we share practical lessons on preparation, local engagement and clear reporting lines that help keep people safe while projects move forward with confidence.</p>
    <span class="arrow"></span>
  </article>
  <article class="post" style="left:620px;padding-left:118px">
    <div class="date-badge">24 June<br>2016</div>
    <h4>BUT I MUST EXPLAIN TO YOU HOW ALL</h4>
    <p>Our consultants recently completed a crisis readiness review for a regional partner, covering emergency planning, staff training and community dialogue to strengthen long term resilience.</p>
    <span class="arrow"></span>
  </article>
</section>

<footer class="site-footer">
  <h2>Get in touch</h2>
  <div class="social-row"><span></span><span></span><span></span><span></span></div>
  <p class="subscribe-note">Subscribe to our newsletter to stay updated with what is new</p>
  <div class="subscribe-input">Email Address</div>
  <span class="btn-subscribe">Subscribe</span>
  <p class="copyright">Copyright 2016 © Kestrel Risk. All Right Reserved</p>
</footer>
</body>
</html>
```